A5 Flyer for Financial Services Business

I am after a re-design of our business flyer to fit in with our new branding style and logo colour scheme. Wanting something with a bit of designer flair that I could not create myself. I have included the flyer which I created which lacks style so dazzle me.

I want to use the same content.

Text for main body of flyer is

Are you a small business owner, tradie or PAVC Service Provider struggling to stay on top of your bookkeeping and compliance obligations? If so we would love to help you get back on track and take control of your business finances so that you can make informed business decisions and focus on what you do best.

We have over 20 years industry experience and, as a small business ourselves, we are able to offer our clients a personal bookkeeping solution tailored to meet the needs of your business.

Accounts Payable | Accounts Receivable
Customer Invoicing
Bank and Credit Card Reconciliations
Payroll | Superannuation | Payroll Tax
Business Activity | Instalment Activity Statements
Regular Financial Reports
Ledgerly and Bookwise Set-Up and Training

```html
<!DOCTYPE html>
<html lang="en">
<head>
<meta charset="utf-8">
<title>Even Ledger Financial Services – Flyer</title>
<link rel="stylesheet" href="https://fonts.googleapis.com/css2?family=Poppins:wght@300;500;600;700&display=swap">
<style>
  :root{
    --stage:#d4d5d7;
    --navy-deep:#0b1628;
    --navy:#12284a;
    --teal:#1d9a96;
    --teal-dark:#13716f;
    --white:#ffffff;
    --ink:#0f1a2b;
    --arrow:#163a5a;
  }
  *{margin:0;padding:0;box-sizing:border-box}
  html,body{width:1200px;height:965px;overflow:hidden;background:var(--stage)}
  body{font-family:'Poppins',sans-serif;position:relative}
  .flyer{position:absolute;left:282px;top:32px;width:636px;height:900px;background:var(--navy-deep);overflow:hidden;box-shadow:0 10px 30px rgba(0,0,0,.25)}
  .flyer-art{position:absolute;inset:0}
  .brand{position:absolute;top:14px;left:0;width:100%;text-align:center;color:var(--white)}
  .brand-mark{display:block;width:58px;height:58px;margin:0 auto 12px;background:var(--white);opacity:.92}
  .brand-name{font-weight:300;font-size:30px;letter-spacing:1px;line-height:1;text-transform:uppercase}
  .brand-tag{font-weight:300;font-size:16px;letter-spacing:5px;line-height:1.4}
  .headline{position:absolute;left:21px;top:232px;color:var(--white);line-height:60px;font-size:60px}
  .headline span{display:block}
  .headline .bold{font-weight:700}
  .headline .light{font-weight:300}
  .headline .accent{font-weight:700;color:var(--teal)}
  .intro{position:absolute;left:21px;top:492px;width:240px;color:var(--white);font-weight:500;font-size:14px;line-height:25px;letter-spacing:.4px}
  .services{position:absolute;right:10px;top:450px;list-style:none;text-align:right}
  .services li{position:relative;height:44px;line-height:28px;padding-right:26px;font-weight:600;font-size:12.5px;color:var(--ink)}
  .services li::after{content:"";position:absolute;right:0;top:7px;border-style:solid;border-width:7px 16px 7px 0;border-color:transparent var(--arrow) transparent transparent}
  .contact{position:absolute;left:22px;top:826px;list-style:none;color:var(--white);font-weight:500;font-size:13px}
  .contact li{display:flex;align-items:center;gap:12px;height:33px}
  .contact svg{width:12px;height:12px;fill:var(--white)}
</style>
</head>
<body>
  <main class="flyer">
    <svg class="flyer-art" width="636" height="900" viewBox="0 0 636 900">
      <defs>
        <radialGradient id="dataGlow" cx="0.72" cy="0.5" r="0.7">
          <stop offset="0" stop-color="#3d6fa6"/>
          <stop offset="0.45" stop-color="#1b3b66"/>
          <stop offset="1" stop-color="#0b1a33"/>
        </radialGradient>
        <linearGradient id="tealBand" x1="0" y1="0" x2="1" y2="0">
          <stop offset="0" stop-color="#1d9a96"/>
          <stop offset="1" stop-color="#13716f"/>
        </linearGradient>
      </defs>
      <rect class="hero-photo" x="0" y="0" width="636" height="560" fill="url(#dataGlow)" role="img" aria-label="Business data dashboard with glowing charts and an open hand reaching up"/>
      <polygon class="shade-diagonal" points="0,330 0,900 268,900 268,457 180,560" fill="#0b1628" opacity=".85"/>
      <rect class="shade-base" x="0" y="560" width="636" height="340" fill="#0b1628"/>
      <polygon class="service-panel" points="636,298 268,457 268,826 355,900 636,900" fill="#ffffff"/>
      <polygon class="contact-band" points="0,826 325,826 355,900 0,900" fill="url(#tealBand)"/>
    </svg>

    <header class="brand">
      <span class="brand-mark"></span>
      <div class="brand-name">Even Ledger</div>
      <div class="brand-tag">Financial Services</div>
    </header>

    <h1 class="headline">
      <span class="bold">Are you a</span>
      <span class="bold">Small</span>
      <span class="light">Business</span>
      <span class="accent">owner?</span>
    </h1>

    <p class="intro">Tradie or PAVC Service Provider struggling to stay on top of your bookkeeping and compliance obligations? If so we would love to help you get back on track and take control of your business finances so that you can make informed business decisions and focus on what you do best.</p>

    <ul class="services">
      <li>Accounts Payable | Accounts Receivable</li>
      <li>Customer Invoicing</li>
      <li>Bank and Credit Card Reconciliations</li>
      <li>Payroll | Superannuation | Payroll Tax</li>
      <li>Business Activity | Instalment Activity Statements</li>
      <li>Regular Financial Reports</li>
      <li>Ledgerly and Bookwise Set-Up and Training</li>
    </ul>

    <ul class="contact">
      <li>
        <svg viewBox="0 0 24 24"><path d="M6.6 10.8a15.1 15.1 0 0 0 6.6 6.6l2.2-2.2a1 1 0 0 1 1-.25 11.4 11.4 0 0 0 3.6.57 1 1 0 0 1 1 1V20a1 1 0 0 1-1 1A17 17 0 0 1 3 4a1 1 0 0 1 1-1h3.5a1 1 0 0 1 1 1c0 1.25.2 2.45.57 3.57a1 1 0 0 1-.25 1z"/></svg>
        0400 123 456
      </li>
      <li>
        <svg viewBox="0 0 24 24"><path d="M4 2l16 9-7 1.5 4 8-3 1.5-4-8L4 19z"/></svg>
        www.evenledgerfinancial.com.au
      </li>
    </ul>
  </main>
</body>
</html>
```